Hip Music Management Co. BIz Card

I have a logo (attached) the back side of the card should the full logo on the entire card- that's it. The front side of the card should show the logo somewhere, keeping with the 4 different shades of blue. The front side of the card can be a white background with logo and colored typeface for all info. Pretty simple.

Target Market(s)

I manage and produce a whole bunch of major label and indie artists.

Industry/Entity Type

Management

Contact Information for Business Card

Velmora Sound House (logo)
Dale Fornwick
President
www.velmorasoundhouse.com
dale@velmorasoundhouse.com
+1 310.555.7182
418 Willow Bend Lane
Ashgrove Falls, NY 10599

Requirements
Must have
• Entire logo on back side. White background on front- unless you provide something more interesting.
Nice to have
• On the front of the card if you choose a white backgound, if possible take my logo without the blue background (over white) that would be cool.

```html
<!DOCTYPE html>
<html lang="en">
<head>
<meta charset="utf-8">
<title>Velmora Sound House – Business Card</title>
<link rel="stylesheet" href="https://fonts.googleapis.com/css2?family=Lato:wght@400;700;900&display=swap">
<style>
  :root {
    --navy: #1a2456;
    --teal: #14b6c4;
    --sky: #72cdf0;
    --mid-blue: #1f7fc0;
    --ink: #1b2350;
    --paper: #ffffff;
    --stage: #e9ebef;
  }
  * { box-sizing: border-box; margin: 0; padding: 0; }
  html, body {
    width: 1200px; height: 1023px; overflow: hidden;
    background: var(--stage);
    font-family: "Lato", Arial, sans-serif;
  }
  .sheet {
    width: 1200px; height: 1023px;
    display: flex; flex-direction: column; align-items: center; justify-content: center; gap: 50px;
  }
  .card {
    position: relative; width: 700px; height: 400px; overflow: hidden;
    box-shadow: 0 6px 18px rgba(20, 30, 70, .18);
  }
  .card-back {
    background: var(--navy);
    display: flex; align-items: center; justify-content: center;
  }
  .brand-name {
    font-weight: 900; color: var(--sky); letter-spacing: .5px; line-height: 1;
  }
  .card-back .brand-name { font-size: 54px; }
  .card-front { background: var(--navy); }
  .card-front .waves { position: absolute; inset: 0; width: 700px; height: 400px; }
  .card-front .brand-name {
    position: absolute; left: 40px; top: 48px; font-size: 50px;
  }
  .holder {
    position: absolute; right: 70px; top: 208px; text-align: center;
  }
  .holder-name { color: var(--sky); font-size: 25px; font-weight: 400; letter-spacing: .5px; }
  .holder-title { color: var(--paper); font-size: 19px; margin-top: 6px; }
  .contact {
    position: absolute; left: 40px; top: 262px;
    color: var(--ink); font-size: 17px; line-height: 24px;
  }
  .contact .label { color: var(--mid-blue); }
  .contact .address { margin-bottom: 6px; line-height: 20px; }
</style>
</head>
<body>
<main class="sheet">
  <section class="card card-back" aria-label="Card back">
    <span class="brand-name">Velmora Sound House</span>
  </section>

  <section class="card card-front" aria-label="Card front">
    <svg class="waves" viewBox="0 0 700 400" aria-hidden="true">
      <path d="M0 232 C140 170 320 205 540 305 C380 270 180 200 0 258 Z" fill="var(--teal)"/>
      <path d="M0 268 C150 215 330 265 480 305 C580 330 650 300 700 272 L700 400 L0 400 Z" fill="var(--paper)"/>
    </svg>
    <span class="brand-name">Velmora Sound House</span>
    <div class="holder">
      <p class="holder-name">DALE FORNWICK</p>
      <p class="holder-title">President</p>
    </div>
    <div class="contact">
      <p class="address">418 Willow Bend Lane<br>Ashgrove Falls, NY 10599</p>
      <p><span class="label">phone:</span> +1 310.555.7182</p>
      <p><span class="label">email:</span> dale@velmorasoundhouse.com</p>
      <p><span class="label">url:</span> www.velmorasoundhouse.com</p>
    </div>
  </section>
</main>
</body>
</html>
```